New letter head for Air Conditioning business

We need a new professional letter head design to suit our new re-branded air conditioning business. Our new logo is attached

```html
<!DOCTYPE html>
<html lang="en">
<head>
<meta charset="utf-8">
<title>Corvane Letterhead</title>
<link href="https://fonts.googleapis.com/css2?family=Poppins:wght@400;500;600;700&display=swap" rel="stylesheet">
<style>
  :root {
    --backdrop: #e4e4e4;
    --paper: #ffffff;
    --ink: #141414;
    --brand-green: #6cc28a;
    --brand-dark: #3f3f42;
    --signature-tone: #e9e9e9;
  }
  * { margin: 0; padding: 0; box-sizing: border-box; }
  html, body {
    width: 1200px; height: 1200px; overflow: hidden;
    background: var(--backdrop);
    font-family: "Poppins", sans-serif;
    color: var(--ink);
  }
  .letterhead {
    position: absolute; left: 197px; top: 30px;
    width: 805px; height: 1140px;
    background: var(--paper);
    box-shadow: 0 6px 24px rgba(0,0,0,0.12);
  }
  .brand {
    position: absolute; left: 50px; top: 68px;
    display: flex; align-items: center; gap: 12px;
  }
  .brand-dot {
    width: 34px; height: 34px; border-radius: 50%;
    background: var(--brand-green);
  }
  .brand-name {
    font-weight: 600; font-size: 34px; letter-spacing: 3px;
    color: var(--brand-dark); line-height: 1;
  }
  .recipient-name {
    position: absolute; left: 56px; top: 258px;
    font-weight: 700; font-size: 20px;
  }
  .letter-date {
    position: absolute; right: 53px; top: 258px;
    font-weight: 700; font-size: 20px;
  }
  .recipient-address {
    position: absolute; left: 56px; top: 294px;
    font-weight: 500; font-size: 20px;
  }
  .letter-body {
    position: absolute; left: 51px; top: 347px; width: 702px;
    font-size: 15.6px; line-height: 18.8px; text-align: justify;
  }
  .letter-body p + p { margin-top: 27px; }
  .closing {
    position: absolute; left: 56px; top: 686px;
    font-weight: 500; font-size: 20px;
  }
  .signature {
    position: absolute; left: 51px; top: 742px;
    width: 170px; height: 58px;
    background: var(--signature-tone); border-radius: 4px;
  }
  .signer {
    position: absolute; left: 51px; top: 828px;
    font-weight: 500; font-size: 20px; line-height: 35px;
  }
  .contact-list {
    position: absolute; right: 60px; top: 918px;
    list-style: none;
  }
  .contact-item {
    display: flex; align-items: center; justify-content: flex-end;
    gap: 30px; height: 28px; margin-bottom: 14.5px;
    font-size: 16px; font-weight: 500;
  }
  .contact-icon { width: 28px; height: 28px; flex: none; }
  .footer-band {
    position: absolute; top: 1117px; height: 23px;
  }
  .footer-band--green { left: 0; width: 245px; background: var(--brand-green); }
  .footer-band--dark { left: 259px; right: 0; background: var(--brand-dark); }
</style>
</head>
<body>
  <main class="letterhead">
    <header class="brand">
      <span class="brand-dot"></span>
      <span class="brand-name">CORVANE</span>
    </header>

    <div class="recipient-name">Your&nbsp; Name Here</div>
    <div class="letter-date">Date : 4.6.2021</div>
    <div class="recipient-address">Address</div>

    <section class="letter-body">
      <p>Lorem ipsum dolor sit amet, consectetur adipiscing elit. Nam pretium quam eget feugiat tincidunt. Nullam consequat mi vitae pharetra sagittis. Suspendisse porta placerat velit, ac condimentum felis molestie in. Nullam eget velit in erat consectetur semper vitae ac nisi. Donec et lectus ut purus aliquam pulvinar non in arcu. Vestibulum et turpis a nisl placerat euismod. Aliquam eu quam augue. Cras consectetur, velit ut semper aliquam, odio tortor suscipit nulla, et vulputate dui risus at ante. Maecenas ac dignissim ex. Pellentesque in dignissim massa. Fusce at posuere lorem. Vivamus molestie nisl ac nisi rhoncus vulputate. Aenean augue arcu, maximus ut consequat in, lobortis sit amet lectus. Suspendisse dapibus auctor quam, sed tempor orci euismod accumsan. In hac habitasse platea dictumst. Suspendisse ut enim metus.</p>
      <p>Nullam at mi eros. Lorem ipsum dolor sit amet, consectetur adipiscing elit. Vestibulum tempus, sem id pharetra ultrices, magna nulla aliquet sapien, ac fringilla odio tortor in eros. Duis a urna sem. Nunc ac purus mattis, pharetra urna quis, ultrices quam. Proin ac sollicitudin dolor, ac feugiat turpis. Sed aliquet ornare nisi, vitae finibus tortor vehicula auctor.</p>
    </section>

    <div class="closing">Regards</div>
    <div class="signature" role="img" aria-label="Handwritten signature"></div>
    <div class="signer">
      <div>Your Name Here</div>
      <div>Designation Here</div>
    </div>

    <ul class="contact-list">
      <li class="contact-item">
        <span>+12345689</span>
        <svg class="contact-icon" viewBox="0 0 28 28" aria-hidden="true">
          <circle cx="14" cy="14" r="14" fill="var(--brand-green)"/>
          <path d="M9.5 7.5c.6-.4 1.3-.3 1.7.3l1.4 2.2c.3.5.2 1.1-.2 1.5l-.9.8c.7 1.6 2 2.9 3.6 3.7l.8-.9c.4-.4 1-.5 1.5-.2l2.2 1.4c.6.4.7 1.1.3 1.7l-.8 1.1c-.5.7-1.4 1-2.2.8-4.3-1.2-7.6-4.5-8.7-8.8-.2-.8.1-1.6.8-2.1z" fill="#fff"/>
        </svg>
      </li>
      <li class="contact-item">
        <span>www.yourwebsite.com</span>
        <svg class="contact-icon" viewBox="0 0 28 28" aria-hidden="true">
          <circle cx="14" cy="14" r="14" fill="var(--brand-green)"/>
          <g fill="none" stroke="#fff" stroke-width="1.4">
            <circle cx="14" cy="14" r="8.5"/>
            <ellipse cx="14" cy="14" rx="3.8" ry="8.5"/>
            <line x1="5.5" y1="14" x2="22.5" y2="14"/>
            <path d="M7 9.5h14M7 18.5h14"/>
          </g>
        </svg>
      </li>
      <li class="contact-item">
        <span>yourgmail@.com</span>
        <svg class="contact-icon" viewBox="0 0 28 28" aria-hidden="true">
          <circle cx="14" cy="14" r="14" fill="var(--brand-green)"/>
          <g fill="none" stroke="#fff" stroke-width="1.3">
            <rect x="7.5" y="9.5" width="13" height="9"/>
            <path d="M7.5 9.5l6.5 5 6.5-5M7.5 18.5l4.7-4.3M20.5 18.5l-4.7-4.3"/>
          </g>
        </svg>
      </li>
    </ul>

    <div class="footer-band footer-band--green"></div>
    <div class="footer-band footer-band--dark"></div>
  </main>
</body>
</html>
```